Bay Area Construction Company

Rebrand existing business card with company colors (Red and gold) for our 100th year.
Updates

Project Deadline Extended
Reason: Lots of good ideas! Still refining the concept, with just a little more time I think we will figure out which one is perfect, thank you.

Project Deadline Extended
Reason: Still reviewing

Project Deadline Extended
Reason: Still reviewing

Project Deadline Extended
Reason: Need business cards to feature updated logo with '100 years' banner.

Project Deadline Extended

Project Deadline Extended

Target Market(s)

Construction industry, males, ages 30-60 who work for building contractors

Industry/Entity Type

Business

Font styles to use
Serif

Colors
ec1f27
fbee3e
ffffff

Requirements
Must have
• Must have the colors red, gold, and black using our existing logo (Logo is available at www.marvenstoneworks.com )
Nice to have
• Company name, try to use something construction oriented. (Hardhat, Bulldoze, etc.)

```html
<!DOCTYPE html>
<html lang="en">
<head>
<meta charset="utf-8">
<title>Marven Stoneworks — Business Card</title>
<link rel="stylesheet" href="https://fonts.googleapis.com/css2?family=Crimson+Pro:wght@400;600;700&display=swap">
<style>
  :root {
    --backdrop: #020b4f;
    --card: #ffffff;
    --red: #d71f27;
    --gold: #f5ee3e;
    --ink: #1a1a1a;
    --navy: #233f94;
    --sign: #f4e21c;
  }
  * { margin: 0; padding: 0; box-sizing: border-box; }
  html, body { width: 1200px; height: 1200px; overflow: hidden; }
  body {
    background: var(--backdrop);
    font-family: "Crimson Pro", Georgia, serif;
    color: var(--ink);
    position: relative;
  }
  .card {
    position: absolute;
    left: 172px;
    width: 857px;
    height: 492px;
    background: var(--card);
    box-shadow: 0 3px 8px rgba(0,0,0,0.45);
    overflow: hidden;
  }
  .card--front { top: 74px; }
  .card--back { top: 624px; }

  .stripe {
    position: absolute;
    top: 87px;
    height: 131px;
    background: var(--gold);
  }
  .stripe::after {
    content: "";
    position: absolute;
    left: 0; right: 0;
    top: 29px;
    height: 73px;
    background: var(--red);
  }
  .stripe--left { left: 0; width: 200px; }
  .stripe--right { right: 0; width: 200px; }

  .brand-name {
    position: absolute;
    left: 200px;
    width: 457px;
    top: 100px;
    height: 105px;
    display: flex;
    align-items: center;
    justify-content: center;
    gap: 12px;
    font-weight: 700;
    font-size: 34px;
    letter-spacing: 1px;
    white-space: nowrap;
    color: var(--navy);
    text-transform: uppercase;
  }
  .brand-mark {
    width: 20px; height: 20px;
    background: var(--navy);
    flex: none;
  }

  .sign {
    position: absolute;
    left: 76px;
    width: 100px;
    height: 100px;
    transform: rotate(45deg);
    background: var(--sign);
    border: 5px solid #111;
    border-radius: 8px;
  }
  .card--front .sign { top: 326px; }
  .card--back .sign { top: 325px; }

  .details {
    position: absolute;
    left: 218px;
    top: 316px;
    display: flex;
    align-items: stretch;
    white-space: nowrap;
  }
  .address, .contact {
    font-size: 22px;
    line-height: 37px;
    padding-top: 4px;
  }
  .address .company { font-weight: 600; font-size: 23px; }
  .divider {
    width: 2px;
    height: 116px;
    margin: 0 26px 0 22px;
    background: #111;
    flex: none;
  }

  .social {
    position: absolute;
    left: 218px;
    top: 312px;
    list-style: none;
    font-size: 22px;
    white-space: nowrap;
  }
  .social li {
    display: flex;
    align-items: center;
    height: 44px;
  }
  .social .network {
    width: 140px;
    font-weight: 700;
    font-size: 22px;
  }
</style>
</head>
<body>

<section class="card card--front">
  <div class="stripe stripe--left"></div>
  <div class="stripe stripe--right"></div>
  <div class="brand-name"><span class="brand-mark"></span>Marven Stoneworks</div>

  <div class="sign" role="img" aria-label="Yellow road-work warning sign with a digging worker"></div>

  <div class="details">
    <div class="address">
      <div class="company">Marven Stoneworks, Inc.</div>
      <div>418 Calder Street</div>
      <div>Harlow Bay, CA 94907</div>
    </div>
    <div class="divider"></div>
    <div class="contact">
      <div>Phone: 415.555.0142</div>
      <div>Fax: 415.555.0178</div>
      <div>Email: info@marvenstoneworks.com</div>
    </div>
  </div>
</section>

<section class="card card--back">
  <div class="stripe stripe--left"></div>
  <div class="stripe stripe--right"></div>
  <div class="brand-name"><span class="brand-mark"></span>Marven Stoneworks</div>

  <div class="sign" role="img" aria-label="Yellow safety sign showing a hard hat"></div>

  <ul class="social">
    <li><span class="network">Clipstream</span><span>clipstream.com/MarvenStoneworks</span></li>
    <li><span class="network">Friendwall</span><span>friendwall.com/MarvenStoneworks</span></li>
    <li><span class="network">Workline</span><span>workline.com/company/marven-stoneworks-inc</span></li>
  </ul>
</section>

</body>
</html>
```